Event Program Design

We are looking to create a stunning event program for “Velvet Gala Night,” presented by The Marlow Chamber Society. This program will reflect the upscale theme of the event while maintaining a clean, elegant layout. We will use a past year’s program as a reference to replicate a similar structure and overall flow, including all page layouts. The cover design will incorporate both front and back, with an inside cover that carries through the sophisticated look established on the front.
Because there are 31 individuals to feature, along with group photos, the program will require enough pages to accommodate everyone without feeling overcrowded (use previous design for reference).
We also have inspirational images and the event invitation available for reference. Please note that these images are for layout purposes only and should not be used for any design elements in the new design—they are solely meant to inspire the final product’s style and color palette.
We plan to base the program’s color scheme on the invitation’s aesthetic; however, we want to avoid directly copying any design features from the reference images or the previous year’s sample. Font selections should complement the elegant theme and must be free to download and use commercially.
The new design should set up for 8 x 11 print size, full color. Please include adequate bleed for print. Will be using prindle for printing so please contact them for any additional questions.
Our goal is a cohesive, refined program that helps attendees navigate the evening’s events while reflecting the grandeur of The Marlow Chamber Society’s “Velvet Gala Night.” We look forward to a layout that strikes the perfect balance between classic sophistication and modern flair—something as memorable as the event itself.

```html
<!DOCTYPE html>
<html lang="en">
<head>
<meta charset="utf-8">
<title>Velvet Gala Night – Program Pages</title>
<link rel="stylesheet" href="https://fonts.googleapis.com/css2?family=Great+Vibes&family=Josefin+Sans:wght@600&family=Libre+Baskerville:wght@400;700&family=Poppins:wght@400;500;600&display=swap">
<style>
:root{
  --board:#525252;
  --paper:#fffdfb;
  --blush:#fbe6da;
  --peach:#f6cfbb;
  --rose:#f0a585;
  --rust:#b8583a;
  --gold:#b8862b;
  --gold-light:#e4c165;
  --ink:#1c1c1c;
  --script:"Great Vibes",cursive;
  --caps:"Josefin Sans",sans-serif;
  --serif:"Libre Baskerville",serif;
  --sans:"Poppins",sans-serif;
}
*{margin:0;padding:0;box-sizing:border-box}
html,body{width:1200px;height:2367px;overflow:hidden;background:var(--board)}
.board{position:relative;width:1200px;height:2367px}
.page{position:absolute;width:473px;height:650px;overflow:hidden;background:var(--paper);box-shadow:6px 8px 14px rgba(0,0,0,.35)}
.wash{position:absolute;inset:0;background:
  radial-gradient(closest-side at 15% 20%,rgba(246,207,187,.75),transparent),
  radial-gradient(closest-side at 85% 85%,rgba(246,207,187,.8),transparent),
  radial-gradient(closest-side at 60% 55%,rgba(251,230,218,.6),transparent)}
.art{position:absolute}
.art.floral{background:radial-gradient(closest-side,rgba(240,165,133,.85),rgba(246,207,187,.55) 55%,rgba(251,230,218,0))}
.art.roses{background:radial-gradient(closest-side,rgba(239,159,120,.85),rgba(246,190,160,.5) 55%,rgba(251,230,218,0))}
.art.leaves{background:radial-gradient(closest-side,rgba(184,88,58,.45),rgba(184,88,58,0))}
.art.glint{background:radial-gradient(closest-side,rgba(228,193,101,.55),rgba(228,193,101,0))}
.art.lattice{background:#faf5ee}
.art.lineart{background:radial-gradient(closest-side,rgba(228,193,101,.25),rgba(228,193,101,0))}
.art.flourish{background:linear-gradient(90deg,transparent,var(--gold-light),transparent);height:4px;border-radius:2px}
svg.lines{position:absolute;inset:0;width:100%;height:100%}
.center{position:absolute;left:0;right:0;text-align:center}
.invite{font-family:var(--caps);font-size:11.5px;letter-spacing:2px;color:var(--gold);line-height:15px}
.script{font-family:var(--script);color:var(--gold);font-weight:400}
.datebar{font-family:var(--serif);font-weight:700;color:var(--gold);display:flex;justify-content:center;align-items:center;gap:10px}
.datebar .rule{width:1px;height:30px;background:var(--gold)}
.datebar sup{font-size:.55em}
.label{font-family:var(--caps);font-size:11px;letter-spacing:2px;color:var(--gold)}
.small{font-family:var(--sans);font-size:9.5px;color:var(--ink);line-height:11.5px}
.names{position:absolute;list-style:none;font-family:var(--serif);font-size:8px;color:var(--ink)}
.names li{height:21px;display:flex;align-items:center;gap:6px}
.tick{width:9px;height:9px;border-radius:50%;background:var(--gold);flex:none;position:relative}
.tick::after{content:"";position:absolute;left:3px;top:1.5px;width:2px;height:4px;border:solid #fff;border-width:0 1.3px 1.3px 0;transform:rotate(45deg)}
.beaux{position:absolute;left:0;right:0;top:300px;text-align:center;font-family:var(--serif);font-weight:700;font-size:13px;color:var(--ink)}
.beaux li{list-style:none;height:47px;display:flex;flex-direction:column;align-items:center;justify-content:flex-end;gap:6px;padding-bottom:6px}
.form{position:absolute;font-family:var(--sans);font-size:9.5px;color:var(--ink)}
.opt{display:flex;align-items:center;gap:8px;height:20px}
.opt b{font-weight:600}
.box{width:28px;height:11px;border:1px solid #c9a789}
.field{display:flex;align-items:center;height:22px}
.field span{width:46px}
.field i{width:146px;height:11px;border:1px solid #d9b79a}
.blank{display:inline-block;border-bottom:1px solid var(--ink);margin-right:4px;vertical-align:bottom}
.pill{font-family:var(--serif);font-weight:700;font-size:9.5px;letter-spacing:1px;color:#fff;background:linear-gradient(90deg,#9a6b1c,var(--gold-light),#9a6b1c);border-radius:8px;padding:3px 10px;display:inline-block}
</style>
</head>
<body>
<main class="board">

  <!-- Front cover -->
  <section class="page" style="left:97px;top:140px">
    <div class="wash"></div>
    <div class="art floral" role="img" aria-label="Watercolor peach lilies with sage leaves" style="left:150px;top:-80px;width:380px;height:330px"></div>
    <div class="art floral" role="img" aria-label="Watercolor peach lily in corner" style="left:-80px;top:480px;width:220px;height:240px"></div>
    <div class="art glint" role="img" aria-label="Gold party sparkle accent" style="left:40px;top:30px;width:110px;height:110px"></div>
    <div class="art glint" role="img" aria-label="Gold party sparkle accent" style="left:400px;top:260px;width:140px;height:140px"></div>
    <svg class="lines" viewBox="0 0 473 650" aria-hidden="true">
      <g fill="none" stroke="var(--gold)" stroke-width="2">
        <polygon points="125,110 395,200 435,470 315,620 60,545 40,360"/>
        <polygon points="150,140 420,150 470,430 360,600 75,470 55,240"/>
      </g>
    </svg>
    <p class="center invite" style="top:216px">YOU ARE CORDIALLY INVITED<br>TO ATTEND A</p>
    <h1 class="center script" style="top:250px;font-size:72px;line-height:70px">Velvet Gala<br>Night</h1>
    <div class="center datebar" style="top:460px;font-size:20px"><span>8<sup>TH</sup></span><i class="rule"></i><span>FEBRUARY</span><i class="rule"></i><span>2025</span></div>
  </section>

  <!-- Back cover -->
  <section class="page" style="left:630px;top:140px">
    <div class="wash"></div>
    <svg class="lines" viewBox="0 0 473 650" aria-hidden="true">
      <g fill="none" stroke="var(--gold)" stroke-width="2">
        <polygon points="140,110 330,80 375,165 410,410 310,530 150,525 65,450 95,200"/>
        <polygon points="165,95 355,115 400,230 395,455 270,555 120,540 85,430 110,170"/>
      </g>
    </svg>
    <div class="art floral" role="img" aria-label="Watercolor lily cluster on frame top" style="left:130px;top:0;width:220px;height:210px"></div>
    <div class="art floral" role="img" aria-label="Watercolor lily cluster on frame bottom" style="left:130px;top:430px;width:220px;height:210px"></div>
    <h2 class="center script" style="top:235px;font-size:60px;line-height:54px">Velvet Gala<br>Night</h2>
    <div class="center" style="top:373px"><span style="display:inline-block;width:180px;font-family:var(--serif);font-size:20px;letter-spacing:5px;color:#fff;background:linear-gradient(90deg,transparent,var(--gold-light) 25%,var(--gold) 75%,transparent)">2025</span></div>
  </section>

  <!-- Invitation page -->
  <section class="page" style="left:97px;top:864px">
    <div class="art lattice" role="img" aria-label="Faint diamond lattice pattern" style="inset:0"></div>
    <svg class="lines" viewBox="0 0 473 650" aria-hidden="true">
      <path d="M58 650V230A178 178 0 0 1 415 230V650Z" fill="var(--paper)"/>
      <path d="M58 650V230A178 178 0 0 1 415 230V650Z" fill="rgba(246,207,187,.35)"/>
      <path d="M45 650V230A191 191 0 0 1 428 230V650" fill="none" stroke="var(--gold)" stroke-width="2"/>
    </svg>
    <div class="art roses" role="img" aria-label="Watercolor peach roses with foliage" style="left:230px;top:-70px;width:310px;height:310px"></div>
    <div class="art leaves" role="img" aria-label="Rust and sage leaves" style="left:-40px;top:360px;width:160px;height:200px"></div>
    <div class="art roses" role="img" aria-label="Watercolor peach rose" style="left:-60px;top:500px;width:260px;height:220px"></div>
    <div class="art leaves" role="img" aria-label="Rust leaves" style="left:340px;top:510px;width:180px;height:180px"></div>
    <p class="center invite" style="top:126px">YOU ARE CORDIALLY INVITED<br>TO ATTEND A</p>
    <h2 class="center script" style="top:170px;font-size:56px;line-height:54px">Velvet Gala<br>Night</h2>
    <p class="center small" style="top:307px;font-size:8.5px;line-height:10px">Benefitting The Marlow Chamber Orchestra &amp; Arts In The High Plains<br>Honoring The 2025 Belles And Beaux</p>
    <div class="center datebar" style="top:340px;font-size:21px"><span>8<sup>TH</sup></span><i class="rule"></i><span>FEBRUARY</span><i class="rule"></i><span>SATURDAY</span></div>
    <div class="center" style="top:383px;display:flex;justify-content:center">
      <span style="font-family:var(--serif);font-weight:700;font-size:12px;color:#fff;background:linear-gradient(90deg,#9a6b1c,var(--gold-light));padding:3px 18px;border-radius:10px 0 0 10px">7:30P.M.</span>
      <span style="font-family:var(--serif);font-weight:700;font-size:12px;color:#fff;background:#111;padding:3px 18px;border-radius:0 10px 10px 0">MIDNIGHT</span>
    </div>
    <svg style="position:absolute;left:229px;top:421px" width="14" height="16" viewBox="0 0 14 16" aria-hidden="true"><path d="M7 1a5 5 0 0 0-5 5c0 4 5 8 5 8s5-4 5-8a5 5 0 0 0-5-5z" fill="none" stroke="var(--gold)" stroke-width="2"/><circle cx="7" cy="6" r="1.6" fill="var(--gold)"/></svg>
    <p class="center small" style="top:445px;font-size:9px;line-height:11.5px">Larkspur Hotel &amp; Conference Center<br>410 Linden Avenue Marlow, Texas<br>Dinner Dancing Cocktails.<br>Candy &amp; Popcorn Bar</p>
    <svg class="lines" viewBox="0 0 473 650" aria-hidden="true"><g stroke="var(--gold)" stroke-width=".8"><line x1="140" y1="515" x2="335" y2="515"/><line x1="140" y1="561" x2="335" y2="561"/></g></svg>
    <p class="center" style="top:525px;font-family:var(--serif);font-size:10.5px;line-height:12px;color:var(--gold)">DINNER DANCING COCKTAILS<br>CANDY &amp; POPCORN BAR</p>
    <p class="center" style="top:574px;font-family:var(--sans);font-size:9px;letter-spacing:1.5px">BLACK TIE OPTIONAL</p>
  </section>

  <!-- Senior Belles -->
  <section class="page" style="left:630px;top:864px">
    <div class="art lattice" role="img" aria-label="Faint diamond lattice pattern" style="inset:0"></div>
    <svg class="lines" viewBox="0 0 473 650" aria-hidden="true">
      <path d="M58 650V200A178 120 0 0 1 415 200V650Z" fill="var(--paper)"/>
      <path d="M58 650V200A178 120 0 0 1 415 200V650Z" fill="rgba(246,207,187,.3)"/>
      <path d="M46 650V200A190 130 0 0 1 427 200V650" fill="none" stroke="var(--gold)" stroke-width="2"/>
    </svg>
    <div class="art roses" role="img" aria-label="Garland of watercolor roses and leaves" style="left:-20px;top:-70px;width:520px;height:260px"></div>
    <div class="art leaves" role="img" aria-label="Rust leaves" style="left:-50px;top:440px;width:150px;height:230px"></div>
    <div class="art roses" role="img" aria-label="Watercolor rose" style="left:-50px;top:560px;width:160px;height:140px"></div>
    <div class="art leaves" role="img" aria-label="Rust leaves" style="left:360px;top:490px;width:160px;height:200px"></div>
    <p class="center label" style="top:196px">MARLOW CHAMBER SOCIETY</p>
    <h2 class="center script" style="top:212px;font-size:62px;line-height:66px">Senior Belles</h2>
    <ul class="names" style="left:100px;top:300px">
      <li><i class="tick"></i>Nora Elise Whitcomb</li><li><i class="tick"></i>Lila Grace Harmon</li><li><i class="tick"></i>Ivy Rose Calder</li><li><i class="tick"></i>Clara Jean Moreno</li><li><i class="tick"></i>Madeline Rae Fitzgerald</li><li><i class="tick"></i>Hazel Anne Tolliver</li><li><i class="tick"></i>Piper Lynn Crane</li><li><i class="tick"></i>Quinn Faith Abbott</li><li><i class="tick"></i>June Marie Ellery</li><li><i class="tick"></i>Tessa Faye Holloway</li><li><i class="tick"></i>Delaney Brooke Ashford</li><li><i class="tick"></i>Wren Adele Navarro</li><li><i class="tick"></i>Margot Claire Bennett</li>
    </ul>
    <ul class="names" style="left:256px;top:300px">
      <li><i class="tick"></i>Sadie Kae Linford-Hale</li><li><i class="tick"></i>Vivian Sage Marquez</li><li><i class="tick"></i>Lucy Reese Pemberton</li><li><i class="tick"></i>Elsie Kate Morrow</li><li><i class="tick"></i>Amira Noor Castell</li><li><i class="tick"></i>Elena Sofia Prado</li><li><i class="tick"></i>Hadley Kay Romero</li><li><i class="tick"></i>Emery Jade Rosales</li><li><i class="tick"></i>Callie Hope Sutton</li><li><i class="tick"></i>Ainsley Mae Serrano</li><li><i class="tick"></i>Celeste Anne Vandermeer</li><li><i class="tick"></i>Harper Lane Whitaker</li>
    </ul>
    <div class="art flourish" role="img" aria-label="Gold flourish divider" style="left:147px;top:610px;width:180px"></div>
  </section>

  <!-- Senior Beaux -->
  <section class="page" style="left:97px;top:1578px">
    <div class="art lattice" role="img" aria-label="Faint diamond lattice pattern" style="inset:0"></div>
    <svg class="lines" viewBox="0 0 473 650" aria-hidden="true">
      <path d="M58 650V200A178 120 0 0 1 415 200V650Z" fill="var(--paper)"/>
      <path d="M58 650V200A178 120 0 0 1 415 200V650Z" fill="rgba(246,207,187,.3)"/>
      <path d="M46 650V200A190 130 0 0 1 427 200V650" fill="none" stroke="var(--gold)" stroke-width="2"/>
    </svg>
    <div class="art roses" role="img" aria-label="Garland of watercolor roses and leaves" style="left:-20px;top:-70px;width:520px;height:260px"></div>
    <div class="art leaves" role="img" aria-label="Rust leaves" style="left:-50px;top:480px;width:150px;height:200px"></div>
    <div class="art roses" role="img" aria-label="Watercolor rose" style="left:-50px;top:570px;width:160px;height:130px"></div>
    <div class="art leaves" role="img" aria-label="Rust leaves" style="left:360px;top:510px;width:160px;height:180px"></div>
    <p class="center label" style="top:196px">MARLOW CHAMBER SOCIETY</p>
    <h2 class="center script" style="top:212px;font-size:60px;line-height:66px">Senior Beaux</h2>
    <ul class="beaux">
      <li><i class="tick"></i>Miles Everett Ashby</li><li><i class="tick"></i>Carter Wade Brennan</li><li><i class="tick"></i>Julian Mateo Delgado</li><li><i class="tick"></i>Owen Blake Winslow</li><li><i class="tick"></i>Rhett Cole Harding</li><li><i class="tick"></i>Samuel Reed Whitford II</li>
    </ul>
    <div class="art flourish" role="img" aria-label="Gold flourish divider" style="left:147px;top:610px;width:180px"></div>
  </section>

  <!-- Reply card -->
  <section class="page" style="left:630px;top:1578px">
    <div class="wash"></div>
    <div class="art leaves" role="img" aria-label="Rust leaves" style="left:-50px;top:-40px;width:140px;height:130px"></div>
    <div class="art lineart" role="img" aria-label="Gold line-art flowers" style="left:220px;top:-40px;width:280px;height:230px"></div>
    <div class="art glint" role="img" aria-label="Gold party sparkle accent" style="left:360px;top:70px;width:150px;height:170px"></div>
    <div class="art floral" role="img" aria-label="Watercolor peach lilies with sage leaves" style="left:300px;top:340px;width:260px;height:360px"></div>
    <h2 class="script" style="position:absolute;left:30px;top:85px;font-size:52px;line-height:50px">Velvet Gala<br>Night</h2>
    <div class="form" style="left:33px;top:210px">
      <div class="opt"><i class="box"></i><span><b>$5,500</b> Platinum Table</span></div>
      <div class="opt"><i class="box"></i><span><b>$300</b> Couples Ticket</span></div>
      <div class="opt"><i class="box"></i><span><b>$3,500</b> Gold Table</span></div>
    </div>
    <div class="form" style="left:200px;top:210px">
      <div class="opt"><i class="box"></i><span><b>$100</b> Student Date Ticket</span></div>
      <div class="opt"><i class="box"></i><span><b>$2,000</b> Silver Table</span></div>
      <div class="opt"><span style="border:1px solid #c9a789;padding:0 6px;font-size:6.5px;font-weight:600;letter-spacing:.5px">*MCS BELLES &amp; BEAUX ARE PREPAID</span></div>
    </div>
    <div style="position:absolute;left:33px;top:301px"><span class="pill">PAYMENT INFORMATION</span></div>
    <div class="form" style="left:33px;top:334px;line-height:24.5px">
      <div><i class="blank" style="width:40px"></i>Enclosed is my check made payable to MCS</div>
      <div><i class="blank" style="width:40px"></i>I am unable to attend, please accept my</div>
      <div>Tax deductable donation of &nbsp;$ <i class="blank" style="width:110px;margin-left:4px"></i></div>
      <div><i class="blank" style="width:106px"></i> &nbsp;Please charge my Credit Card</div>
    </div>
    <div class="form" style="left:33px;top:440px">
      <div class="field"><span>Card #</span><i></i></div>
      <div class="field"><span>Exp.</span><i></i></div>
      <div class="field"><span>CVV #</span><i></i></div>
      <div class="field"><span>Zipcode</span><i></i></div>
    </div>
    <p class="form" style="left:33px;top:562px;font-weight:600;font-size:10px;line-height:12.5px">Please return to MCS /<br>Camille Dorsey<br>PO Box 2087 Marlow,<br>TX 79301</p>
  </section>

</main>
</body>
</html>
```